Management consultant needs business cards

We need a design for a personal/professional business card for a management consultant. Work is typically focused on the b2b space, helping companies improve their operations. The final design should communicate efficiency and helping companies and people achieve their full potential.

Company name is "Copperfen Consultants"

Brand promise is "Finding Potential - Unleashing Performance"

We come from major consulting firms (Haldorne, Vesk, TQP) but would like to project a slightly more modern feel than those players.

Target Market(s)

Targeting B2B markets such as banks or companies.

Industry/Entity Type

Business

Requirements
Must have
• The card must communicate the following information:

Nolan J Brackett
Managing Director
Copperfen Consultants
Phone: 416-555-0172
nolan.brackett@copperfenconsultants.example
www.copperfenconsultants.example

214 Pellworth Ave
Toronto, ON M5X 9Z7

Back side should have
"Finding Potential - Unleashing Performance"

```html
<!DOCTYPE html>
<html lang="en">
<head>
<meta charset="utf-8">
<title>Copperfen Consultants – Business Card</title>
<link rel="stylesheet" href="https://fonts.googleapis.com/css2?family=Arimo:wght@400;700&family=Open+Sans:wght@400;600&display=swap">
<style>
  :root {
    --backdrop: #e6e8ea;
    --teal-light: #22c4bd;
    --teal-mid: #13a19d;
    --teal-dark: #0a6668;
    --teal-ink: #1a9c96;
    --navy: #1f3652;
    --navy-dark: #142539;
    --paper: #f5f5f4;
    --paper-shade: #e4e5e5;
    --ink: #3a3d40;
    --white: #ffffff;
  }
  * { box-sizing: border-box; margin: 0; padding: 0; }
  html, body {
    width: 1200px; height: 902px; overflow: hidden;
    background: var(--backdrop);
  }
  .sheet {
    width: 1200px; height: 902px;
    display: flex; flex-direction: column; align-items: center; justify-content: center;
    gap: 48px;
  }
  .card {
    position: relative;
    width: 640px; height: 366px;
    overflow: hidden;
    box-shadow: 0 10px 28px rgba(0,0,0,.22);
  }

  /* Front */
  .card-front {
    background: radial-gradient(ellipse at 55% 45%, var(--teal-light) 0%, var(--teal-mid) 45%, var(--teal-dark) 100%);
  }
  .team-figures {
    position: absolute; left: 70px; top: 36px; width: 520px; height: 300px;
    background: linear-gradient(90deg, rgba(255,255,255,0) 0%, rgba(190,240,238,.22) 30%, rgba(190,240,238,.22) 70%, rgba(255,255,255,0) 100%);
  }
  .brand-block {
    position: absolute; left: 0; right: 0; top: 150px;
    text-align: center; color: var(--white);
  }
  .brand-name {
    font-family: "Arimo", Arial, sans-serif;
    font-weight: 700; font-size: 46px; letter-spacing: .5px;
    text-shadow: 0 2px 3px rgba(0,0,0,.25);
  }
  .brand-promise {
    margin-top: 6px;
    font-family: "Open Sans", Arial, sans-serif;
    font-size: 16px;
  }

  /* Back */
  .card-back {
    background: linear-gradient(135deg, var(--white) 0%, var(--paper) 50%, var(--paper-shade) 100%);
  }
  .world-texture {
    position: absolute; left: 40px; top: 20px; width: 560px; height: 220px;
    background: radial-gradient(ellipse at center, rgba(200,204,206,.35) 0%, rgba(200,204,206,0) 70%);
  }
  .details {
    position: absolute; left: 250px; top: 34px; width: 360px;
    font-family: "Open Sans", Arial, sans-serif; color: var(--ink);
  }
  .person-name {
    font-family: "Open Sans", Arial, sans-serif;
    font-variant: small-caps;
    font-size: 25px; font-weight: 600; letter-spacing: 3px;
    color: var(--teal-ink);
  }
  .person-role { font-size: 12px; margin-top: 0; margin-left: 2px; }
  .rule { height: 1px; background: var(--teal-ink); margin: 10px 0 12px; }
  .contact-list { list-style: none; }
  .contact-item {
    display: flex; align-items: flex-start; gap: 10px;
    font-size: 12px; line-height: 16px; margin-bottom: 7px;
  }
  .contact-icon { flex: 0 0 16px; width: 16px; height: 16px; }
  .rule-end { margin: 6px 0 0; width: 70%; }
  .name-band {
    position: absolute; left: 0; right: 0; bottom: 58px; height: 64px;
    background: linear-gradient(180deg, var(--navy) 0%, var(--navy-dark) 100%);
    display: flex; align-items: center; justify-content: center;
  }
  .band-name {
    font-family: "Arimo", Arial, sans-serif;
    font-weight: 700; font-size: 30px; color: var(--white); letter-spacing: .5px;
  }
</style>
</head>
<body>
<main class="sheet">

  <section class="card card-front" aria-label="Card front">
    <div class="team-figures" role="img" aria-label="Row of faint standing business people silhouettes"></div>
    <div class="brand-block">
      <h1 class="brand-name">Copperfen Consultants</h1>
      <p class="brand-promise">Finding Potential - Unleashing Performance</p>
    </div>
  </section>

  <section class="card card-back" aria-label="Card back">
    <div class="world-texture" role="img" aria-label="Faint world map texture"></div>
    <div class="details">
      <h2 class="person-name">Nolan J Brackett</h2>
      <p class="person-role">Managing Director</p>
      <div class="rule"></div>
      <ul class="contact-list">
        <li class="contact-item">
          <svg class="contact-icon" viewBox="0 0 16 16" aria-hidden="true"><circle cx="8" cy="8" r="8" fill="#1a9c96"/><path d="M5.2 4.2l1.4-.2.7 1.8-.9.7c.4 1 1.1 1.7 2.1 2.1l.7-.9 1.8.7-.2 1.4c-.1.5-.6.8-1.1.7C7 10.1 5.9 9 5.5 6.2c-.1-.5.2-1.9-.3-2z" fill="#fff"/></svg>
          <span>416-555-0172</span>
        </li>
        <li class="contact-item">
          <svg class="contact-icon" viewBox="0 0 16 16" aria-hidden="true"><circle cx="8" cy="8" r="8" fill="#1a9c96"/><rect x="4" y="5" width="8" height="6" fill="#fff"/><path d="M4 5l4 3.2L12 5" fill="none" stroke="#1a9c96" stroke-width=".9"/></svg>
          <span>nolan.brackett@copperfenconsultants.example</span>
        </li>
        <li class="contact-item">
          <svg class="contact-icon" viewBox="0 0 16 16" aria-hidden="true"><circle cx="8" cy="8" r="8" fill="#1a9c96"/><circle cx="8" cy="8" r="4" fill="none" stroke="#fff" stroke-width="1"/><path d="M4 8h8M8 4c-1.6 1.2-1.6 6.8 0 8M8 4c1.6 1.2 1.6 6.8 0 8" fill="none" stroke="#fff" stroke-width=".8"/></svg>
          <span>www.copperfenconsultants.example</span>
        </li>
        <li class="contact-item">
          <svg class="contact-icon" viewBox="0 0 16 16" aria-hidden="true"><circle cx="8" cy="8" r="8" fill="#1a9c96"/><path d="M8 3.5a3 3 0 0 1 3 3c0 2.2-3 5.8-3 5.8S5 8.7 5 6.5a3 3 0 0 1 3-3z" fill="#fff"/><circle cx="8" cy="6.5" r="1.1" fill="#1a9c96"/></svg>
          <span>214 Pellworth Ave, Toronto<br>ON M5X 9Z7</span>
        </li>
      </ul>
      <div class="rule rule-end"></div>
    </div>
    <div class="name-band">
      <p class="band-name">Copperfen Consultants</p>
    </div>
  </section>

</main>
</body>
</html>
```